Upscale business cards needed for family office

We would like professional business cards created for employees of our family office. Relatively simple and straightforward, but also with a unique element to set them apart. Probably stick with neutral and simple colors that mesh well with the colors in the logo. We need space for the traditional elements, including name, title, address, email/phone number.

Industry/Entity Type

Business

Contact Information for Business Card

Space for name, title, phone number, email, address

```html
<!DOCTYPE html>
<html lang="en">
<head>
<meta charset="utf-8">
<title>R&amp;T Business Card</title>
<link rel="stylesheet" href="https://fonts.googleapis.com/css2?family=Arimo:wght@400;700&display=swap">
<style>
  :root {
    --card-bg: #eeeff0;
    --ink: #231f20;
    --brand-grey: #5a5d60;
    --brand-blue: #1e97c4;
    --white: #ffffff;
  }
  html, body {
    margin: 0;
    padding: 0;
    width: 1200px;
    height: 686px;
    overflow: hidden;
    background: var(--card-bg);
  }
  .card {
    position: relative;
    width: 1200px;
    height: 686px;
    background: radial-gradient(ellipse at 40% 40%, #f3f4f5 0%, var(--card-bg) 70%);
    font-family: "Arimo", Arial, sans-serif;
    color: var(--ink);
    overflow: hidden;
  }
  .brand {
    position: absolute;
    left: 84px;
    top: 62px;
    display: flex;
    align-items: center;
    gap: 18px;
  }
  .brand-square {
    width: 40px;
    height: 40px;
    background: var(--brand-blue);
  }
  .brand-name {
    font-size: 66px;
    font-weight: 400;
    color: var(--brand-grey);
    line-height: 1;
  }
  .contact {
    position: absolute;
    right: 80px;
    top: 248px;
    text-align: right;
  }
  .person-name {
    margin: 0;
    font-size: 46px;
    font-weight: 700;
    letter-spacing: 0.02em;
    line-height: 1.1;
  }
  .person-title {
    margin: 4px 0 0;
    font-size: 30px;
    letter-spacing: 0.16em;
    line-height: 1.2;
  }
  .phone-label {
    margin: 24px 0 0;
    font-size: 30px;
    letter-spacing: 0.16em;
    line-height: 1.2;
  }
  .phone-number {
    margin: 2px 0 0;
    font-size: 46px;
    font-weight: 700;
    letter-spacing: 0.02em;
    line-height: 1.15;
  }
  .email {
    margin: 26px 0 0;
    font-size: 34px;
    letter-spacing: 0.17em;
    line-height: 1.2;
  }
  .footer-band {
    position: absolute;
    left: 0;
    bottom: 0;
    width: 1200px;
    height: 130px;
  }
  .address {
    position: absolute;
    right: 74px;
    bottom: 42px;
    margin: 0;
    font-size: 30px;
    letter-spacing: 0.04em;
    color: var(--white);
    white-space: nowrap;
  }
</style>
</head>
<body>
  <div class="card">
    <div class="brand">
      <span class="brand-square"></span>
      <span class="brand-name">R&amp;T</span>
    </div>

    <div class="contact">
      <h1 class="person-name">Daniel Hale</h1>
      <p class="person-title">Managing Director</p>
      <p class="phone-label">Mobile</p>
      <p class="phone-number">1-555-014-2290</p>
      <p class="email">danielhalert@example.com</p>
    </div>

    <svg class="footer-band" viewBox="0 0 1200 130" preserveAspectRatio="none" aria-hidden="true">
      <path d="M0 40 C 300 10, 700 0, 1200 0 L1200 130 L0 130 Z" fill="var(--brand-blue)"/>
    </svg>
    <p class="address">R&amp;T Office 812 Linden Ave Brookfield, ME 04011</p>
  </div>
</body>
</html>
```